BRIMLOW Pizza and Wraps

We need a website for a new restaurant called BRIMLOW "PIZZA AND WRAPS".
I have attached fonts, background images, logo, images, content etc.
can provide you with what you need to get the website design done fast and easy

I have uploaded more images of the venue and some menu items. let me know if there is anything I need to provide to make your mission clear and easy

Reason: i would like a little time to provide more feedback to designers

Industry/Entity Type

Restaurant

Coding

Coded - Design and coding required

Number of Pages Required

5+ page

Colors

Designer to choose colors to be used in the design.

Requirements
Must have
• PAGES:
• Our Story
• Menu
• Reservations
• Catering & Delivery
• Contact

```html
<!DOCTYPE html>
<html lang="en">
<head>
<meta charset="utf-8">
<title>BRIMLOW Pizza and Wraps — Our Story</title>
<link rel="stylesheet" href="https://fonts.googleapis.com/css2?family=Montserrat:wght@500;600;800&family=Playfair+Display:wght@700&family=Open+Sans:wght@400&family=Great+Vibes&display=swap">
<style>
  :root {
    --orange: #f4a11c;
    --orange-deep: #e8870f;
    --active: #a6d22c;
    --brand-red: #d8232a;
    --maroon: #3a1313;
    --maroon-deep: #2a0c0c;
    --paper: #ffffff;
    --heading: #ef7d1a;
    --muted-text: #e9dcd4;
  }
  * { box-sizing: border-box; margin: 0; padding: 0; }
  html, body { width: 1200px; height: 797px; overflow: hidden; background: var(--paper); }
  .site { position: relative; width: 1200px; height: 797px; overflow: hidden; font-family: "Open Sans", sans-serif; }

  .hero { position: absolute; left: 0; top: 0; width: 1200px; height: 400px; }
  .hero__photo {
    position: absolute; inset: 0;
    background:
      radial-gradient(ellipse at 40% 80%, #e2c89a 0%, #c79d63 35%, transparent 70%),
      linear-gradient(180deg, #f2a12a 0%, #d18a3a 18%, #8a5a33 40%, #b98a58 70%, #d9b88a 100%);
  }
  .hero__nav {
    position: absolute; top: 0; left: 0; right: 0; height: 46px;
    background: linear-gradient(180deg, var(--orange) 0%, rgba(244,161,28,0.85) 100%);
    display: flex; justify-content: flex-end; align-items: center; gap: 46px; padding-right: 46px;
    font-family: "Montserrat", sans-serif; font-weight: 600; font-size: 12px; letter-spacing: 2.5px; color: var(--paper);
  }
  .hero__nav a { color: inherit; text-decoration: none; }
  .hero__nav a.is-active { color: var(--active); }

  .brand-frame {
    position: absolute; left: 375px; top: 145px; width: 510px; height: 150px;
    border: 4px solid rgba(255,255,255,0.9);
    background: rgba(255,255,255,0.22);
    display: flex; align-items: center; justify-content: center;
  }
  .brand-frame__name {
    font-family: "Montserrat", sans-serif; font-weight: 800; font-size: 74px;
    letter-spacing: 3px; color: var(--brand-red);
  }

  .story-heading { position: absolute; top: 430px; left: 0; right: 0; text-align: center; }
  .story-heading__title {
    font-family: "Playfair Display", serif; font-weight: 700; font-size: 30px;
    letter-spacing: 2px; color: var(--heading);
  }
  .story-heading__rule { display: block; margin: 6px auto 0; width: 210px; height: 2px; background: var(--heading); }

  .story { position: absolute; left: 0; top: 510px; width: 1200px; height: 287px; }
  .story__photo {
    position: absolute; inset: 0;
    background: linear-gradient(110deg, #6b4a22 0%, #c99a2c 45%, #f6d34e 70%, #fbe38a 100%);
  }
  .story__panel {
    position: absolute; left: 0; top: 0; width: 720px; height: 287px;
    background: linear-gradient(90deg, var(--maroon-deep), var(--maroon));
    clip-path: polygon(0 0, 100% 0, 86% 100%, 0 100%);
    padding: 52px 140px 0 70px;
    color: var(--muted-text); font-size: 12.5px; line-height: 1.7; text-align: center;
  }
  .story__script { font-family: "Great Vibes", cursive; font-size: 26px; line-height: 1.3; color: var(--paper); }
</style>
</head>
<body>
<main class="site">
  <header class="hero">
    <div class="hero__photo" role="img" aria-label="Grilled wraps cut in halves on paper, on a wooden table on a sunny patio"></div>
    <nav class="hero__nav">
      <a class="is-active" href="#story">OUR STORY</a>
      <a href="#menu">MENU</a>
      <a href="#reservations">RESERVATIONS</a>
      <a href="#catering">CATERING &amp; DELIVERY</a>
      <a href="#contact">CONTACT</a>
    </nav>
    <div class="brand-frame">
      <span class="brand-frame__name">BRIMLOW</span>
    </div>
  </header>

  <div class="story-heading" id="story">
    <h2 class="story-heading__title">OUR STORY</h2>
    <span class="story-heading__rule"></span>
  </div>

  <section class="story">
    <div class="story__photo" role="img" aria-label="Restaurant interior with warm yellow ceiling lights and a metal shelf"></div>
    <div class="story__panel">
      <p>Built in heritage, Brimlow is a gathering place celebrating the Mediterranean food tradition.</p>
      <p class="story__script">Brimlow is the ultimate escape</p>
      <p>– the perfect spot to enjoy sensational food and drinks that showcase everything the Mediterranean has to offer in a simple, sophisticated setting.</p>
      <p>Where an early morning walk to the bakery around the corner is a way of life.</p>
    </div>
  </section>
</main>
</body>
</html>
```